Creating a Label for the Wine "Brenola"

Brenola
As you know Brenola is an imagined place or state of things in which everything is perfect. This wine reflects that. It is a high value wine and it is perfect. The dimensions shoulb be between 9c x 11,5 cm and 12cm x 8 cm

```html
<!DOCTYPE html>
<html lang="en">
<head>
<meta charset="utf-8">
<title>Brenola — Red Wine Label</title>
<link rel="stylesheet" href="https://fonts.googleapis.com/css2?family=EB+Garamond:wght@400&display=swap">
<style>
  :root {
    --backdrop: #1b1b1c;
    --label-paper: #f3f3f2;
    --label-paper-shade: #e4e4e3;
    --label-band: #1e1e20;
    --ink-dark: #1e1e20;
    --ink-light: #f1f1f0;
  }
  html, body {
    margin: 0;
    padding: 0;
    width: 1200px;
    height: 3025px;
    overflow: hidden;
    background: var(--backdrop);
  }
  .canvas {
    position: relative;
    width: 1200px;
    height: 3025px;
    display: flex;
    align-items: center;
    justify-content: center;
  }
  .wine-label {
    width: 1000px;
    height: 920px;
    display: flex;
    flex-direction: column;
    font-family: "EB Garamond", "Times New Roman", serif;
  }
  .label-top {
    height: 595px;
    background: linear-gradient(90deg, var(--label-paper-shade) 0%, var(--label-paper) 20%, var(--label-paper) 80%, var(--label-paper-shade) 100%);
    display: flex;
    align-items: flex-end;
    justify-content: center;
    padding-bottom: 70px;
    box-sizing: border-box;
  }
  .brand-mark {
    display: flex;
    align-items: center;
    gap: 22px;
    color: var(--ink-dark);
    font-size: 54px;
    font-weight: 400;
    letter-spacing: 0.12em;
    text-transform: uppercase;
  }
  .brand-mark .dot {
    width: 26px;
    height: 26px;
    border-radius: 50%;
    background: var(--ink-dark);
  }
  .label-band {
    flex: 1;
    background: var(--label-band);
    display: flex;
    flex-direction: column;
    align-items: center;
    color: var(--ink-light);
  }
  .wine-name {
    margin: 28px 0 0;
    font-size: 164px;
    font-weight: 400;
    line-height: 1;
    letter-spacing: 0.03em;
    text-transform: uppercase;
  }
  .wine-type {
    margin: 52px 0 0;
    font-size: 30px;
    font-weight: 400;
    letter-spacing: 0.08em;
    text-transform: uppercase;
  }
</style>
</head>
<body>
  <main class="canvas">
    <section class="wine-label">
      <div class="label-top">
        <div class="brand-mark"><span class="dot"></span>Brenola</div>
      </div>
      <div class="label-band">
        <h1 class="wine-name">Brenola</h1>
        <p class="wine-type">Red Wine</p>
      </div>
    </section>
  </main>
</body>
</html>
```